Logo and bussiness card stationary design

I want bussiness cards ann stationary that would mactch with the design of my website:

drmarcelvantroy.com.au

Logo Text

Dr Marcel Vantroy

```html
<!DOCTYPE html>
<html lang="en">
<head>
<meta charset="utf-8">
<title>Dr Marcel Vantroy – Business Card</title>
<link href="https://fonts.googleapis.com/css2?family=Nunito+Sans:wght@400;600;700;800&display=swap" rel="stylesheet">
<style>
  :root {
    --teal: #4ab3c5;
    --teal-deep: #48b2c4;
    --teal-soft: #b9dde5;
    --ink: #1f3547;
    --tan: #c9a77c;
    --orange: #f28a1f;
    --mint: #93d3c8;
    --ring: #d5d8d9;
    --white: #ffffff;
    --bg-top: #f4f7f8;
    --bg-bottom: #9fd0dc;
  }
  html, body {
    margin: 0;
    padding: 0;
    width: 1200px;
    height: 1000px;
    overflow: hidden;
  }
  body {
    font-family: "Nunito Sans", sans-serif;
    background: linear-gradient(180deg, var(--bg-top) 0%, var(--bg-top) 35%, var(--bg-bottom) 100%);
    position: relative;
  }
  .card {
    position: absolute;
    left: 245px;
    width: 712px;
    height: 405px;
    box-sizing: border-box;
    border: 1px solid #9a9a9a;
    overflow: hidden;
  }
  .card--front { top: 27px; background: var(--white); }
  .card--back { top: 522px; height: 408px; background: var(--teal-deep); }

  .brand {
    position: absolute;
    right: 44px;
    top: 58px;
    text-align: right;
  }
  .brand__name {
    margin: 0;
    font-size: 31px;
    font-weight: 800;
    letter-spacing: 0.5px;
    color: var(--teal);
    line-height: 1;
  }
  .brand__tagline {
    margin: 8px 0 0;
    font-size: 17px;
    font-weight: 600;
    color: var(--ink);
  }
  .phone-band {
    position: absolute;
    left: 0;
    top: 150px;
    width: 100%;
    height: 68px;
    background: var(--teal);
    border-top: 2px solid var(--tan);
    border-bottom: 2px solid var(--tan);
    box-sizing: border-box;
    display: flex;
    align-items: center;
    justify-content: center;
    padding-left: 36px;
    color: var(--white);
    font-size: 28px;
    font-weight: 600;
    letter-spacing: 0.5px;
  }
  .offices {
    position: absolute;
    top: 243px;
    left: 0;
    width: 100%;
    display: flex;
    font-size: 20px;
    font-weight: 600;
    line-height: 27px;
    color: var(--ink);
  }
  .office { margin: 0; font-style: normal; }
  .office--sydney {
    width: 356px;
    text-align: right;
    padding-right: 17px;
    border-right: 2px solid var(--ink);
  }
  .office--melbourne { padding-left: 15px; }
  .website {
    position: absolute;
    top: 360px;
    left: 36px;
    right: 0;
    text-align: center;
    font-size: 25px;
    font-weight: 600;
    color: var(--teal);
  }

  .back-art { position: absolute; inset: 0; }
  .back-title {
    font-family: "Nunito Sans", sans-serif;
    font-weight: 800;
    font-size: 26px;
    fill: var(--white);
    letter-spacing: 0.5px;
  }
  .day-label {
    font-family: "Nunito Sans", sans-serif;
    font-weight: 800;
    font-size: 15px;
    fill: var(--orange);
  }
  .field-label {
    font-family: "Nunito Sans", sans-serif;
    font-weight: 800;
    font-size: 15px;
    fill: var(--ink);
  }
</style>
</head>
<body>

<section class="card card--front" aria-label="Business card front">
  <div class="brand">
    <h1 class="brand__name">DR. MARCEL VANTROY</h1>
    <p class="brand__tagline">Safe and Affordable Oral Surgery</p>
  </div>
  <div class="phone-band">1300 555 046</div>
  <div class="offices">
    <address class="office office--sydney">SYDNEY<br>Suite 6 Level 9, 240<br>Harbour Street<br>Sydney NSW 2000</address>
    <address class="office office--melbourne">MELBOURNE<br>Level 5, 318<br>Garden Street<br>Melbourne VIC 3000</address>
  </div>
  <div class="website">DrMarcelVantroy.com.au</div>
</section>

<section class="card card--back" aria-label="Appointment card back">
  <svg class="back-art" width="712" height="408" viewBox="0 0 712 408" xmlns="http://www.w3.org/2000/svg">
    <text class="back-title" x="356" y="50" text-anchor="middle">YOUR NEXT APPOINTMENT IS ON:</text>

    <circle cx="352" cy="235" r="165" fill="var(--white)"/>

    <g class="day-picker">
      <circle cx="207" cy="95" r="25" fill="var(--white)"/>
      <text class="day-label" x="207" y="100" text-anchor="middle">MON</text>
      <circle cx="168" cy="155" r="25" fill="var(--white)"/>
      <text class="day-label" x="168" y="160" text-anchor="middle">TUE</text>
      <circle cx="153" cy="222" r="25" fill="var(--white)"/>
      <text class="day-label" x="153" y="227" text-anchor="middle">WED</text>
      <circle cx="164" cy="291" r="25" fill="var(--white)"/>
      <text class="day-label" x="164" y="296" text-anchor="middle">THU</text>
      <circle cx="199" cy="356" r="25" fill="var(--white)"/>
      <text class="day-label" x="199" y="361" text-anchor="middle">FRI</text>
    </g>

    <g class="entry-fields">
      <line x1="242" y1="169" x2="453" y2="169" stroke="var(--orange)" stroke-width="2"/>
      <text class="field-label" x="216" y="246">AT</text>
      <line x1="250" y1="246" x2="461" y2="246" stroke="var(--orange)" stroke-width="2"/>
      <text class="field-label" x="391" y="235">AM</text>
      <text class="field-label" x="447" y="235">PM</text>
    </g>

    <circle cx="570" cy="211" r="74" fill="var(--mint)" stroke="var(--ring)" stroke-width="6"/>
  </svg>
</section>

</body>
</html>
```